Design for sports training app

We need the design for 9 screens of an app that supports trainers of sport teams in preparing their training sessions. Regarding colors, fonts etc. there is absolute freedom for the designer to choose what he thinks is best.
The app will be called "Vellix", our idea for the logo is something like a stopwatch.
Wireframes are attached for every screen. You don't have to stick to those - if you have better ideas, we are happy to see them.
Our strategy is "mobile first". Based on the app design we will create a homepage later - I guess it makes sense to give this to the same person, let's see.
The deliverables are attached.
All in all the main target is to present a very simple, intuitive and nice UI that the user can work with without much learning.
Updates
Target Market(s)
Soccer trainers
Industry/Entity Type
Training
Look and feel

```html
<!DOCTYPE html>
<html lang="en">
<head>
<meta charset="utf-8">
<title>Vellix – Offensive 2 vs. 1</title>
<link href="https://fonts.googleapis.com/css2?family=Roboto:wght@300;400;500&display=swap" rel="stylesheet">
<style>
  :root{
    --navy-top:#1d3f60;
    --navy-bottom:#132c48;
    --accent:#1f4a6e;
    --link:#2d5f8c;
    --tab-active:#3e6b90;
    --tab-idle:#9aa3ab;
    --text:#2b2f33;
    --body:#4a4f54;
    --muted:#8a9097;
    --rail:#e3e7eb;
    --dots:#c9ced3;
    --white:#ffffff;
    --grass:#4f8a3c;
    --grass-dark:#3c6d2e;
  }
  *{box-sizing:border-box;margin:0;padding:0}
  html,body{width:708px;height:1200px;overflow:hidden;background:var(--white)}
  body{font-family:"Roboto",Arial,sans-serif;color:var(--text)}
  .screen{position:relative;width:708px;height:1200px;overflow:hidden;background:var(--white)}

  .app-header{position:absolute;left:0;top:0;width:708px;height:140px;
    background:linear-gradient(180deg,var(--navy-top),var(--navy-bottom));color:var(--white)}
  .status-bar{position:absolute;left:0;top:0;width:100%;height:55px;font-size:24px;font-weight:400}
  .status-bar .carrier{position:absolute;left:14px;top:14px;display:flex;align-items:center;gap:8px}
  .status-bar .time{position:absolute;left:0;right:0;top:14px;text-align:center}
  .status-bar .power{position:absolute;right:14px;top:14px;display:flex;align-items:center;gap:10px}
  .nav-bar{position:absolute;left:0;top:55px;width:100%;height:85px}
  .nav-bar .back{position:absolute;left:26px;top:26px}
  .nav-bar h1{position:absolute;left:0;right:0;top:24px;text-align:center;font-size:31px;font-weight:400;letter-spacing:.2px}

  .timeline-rail{position:absolute;left:33px;top:140px;width:5px;height:955px;background:var(--rail)}
  .divider{position:absolute;left:66px;width:624px;border-top:2px dotted var(--dots)}
  .node{position:absolute;left:14px;width:43px;height:43px;border-radius:50%;background:var(--accent);
    display:flex;align-items:center;justify-content:center}

  .media{position:absolute;left:66px;width:622px;
    background:linear-gradient(180deg,#6e8f5e 0%,var(--grass) 45%,var(--grass-dark) 100%)}
  .media.hero{top:140px;height:152px}
  .media.video{left:70px;top:580px;width:618px;height:272px;
    background:linear-gradient(180deg,#3b3a3e 0%,#56604f 38%,var(--grass) 60%,var(--grass-dark) 100%)}
  .play{position:absolute;left:278px;top:105px;width:62px;height:62px;border-radius:50%;
    background:rgba(255,255,255,.28);display:flex;align-items:center;justify-content:center}

  .drill-title{position:absolute;left:68px;top:336px;font-size:28px;font-weight:300;color:var(--text)}
  .copy{position:absolute;left:68px;width:622px;font-size:15.5px;line-height:24.4px;font-weight:300;color:var(--body)}
  .copy.intro{top:378px}
  .copy.caption{top:876px}

  .resource{position:absolute;left:70px;top:988px}
  .resource .source{font-size:12px;color:var(--muted);font-weight:300}
  .resource .url{display:block;margin-top:4px;font-size:16.5px;color:var(--link);font-weight:300;text-decoration:none}
  .resource .note{margin-top:6px;font-size:16px;color:var(--body);font-weight:300}

  .tab-bar{position:absolute;left:0;top:1095px;width:708px;height:105px;background:#f8f9fa;border-top:1px solid #e6e9ec;display:flex}
  .tab{flex:1;display:flex;flex-direction:column;align-items:center;padding-top:16px;font-size:16px;color:var(--tab-idle);gap:6px}
  .tab.active{color:var(--tab-active)}
  .tab-indicator{position:absolute;left:0;bottom:0;width:202px;height:4px;background:var(--tab-active)}
</style>
</head>
<body>
<main class="screen">
  <header class="app-header">
    <div class="status-bar">
      <div class="carrier">
        <svg width="74" height="14" viewBox="0 0 74 14"><g fill="#fff"><circle cx="7" cy="7" r="6"/><circle cx="22" cy="7" r="6"/><circle cx="37" cy="7" r="6"/></g><g fill="none" stroke="#fff" stroke-width="1.5"><circle cx="52" cy="7" r="5.3"/><circle cx="67" cy="7" r="5.3"/></g></svg>
        <span>NOVA</span>
        <svg width="26" height="20" viewBox="0 0 26 20" fill="none" stroke="#fff" stroke-width="2.6" stroke-linecap="round"><path d="M2 7a16 16 0 0 1 22 0"/><path d="M6 11a10 10 0 0 1 14 0"/><path d="M10 15a4 4 0 0 1 6 0"/></svg>
      </div>
      <div class="time">4:21 PM</div>
      <div class="power">
        <svg width="16" height="26" viewBox="0 0 16 26" fill="none" stroke="#8fa3b6" stroke-width="2"><path d="M2 7l12 11-6 6V2l6 6L2 19"/></svg>
        <span>22%</span>
        <svg width="54" height="24" viewBox="0 0 54 24"><rect x="1" y="2" width="47" height="20" rx="3" fill="none" stroke="#fff" stroke-width="2"/><rect x="4" y="5" width="10" height="14" fill="#fff"/><rect x="49.5" y="8" width="3" height="8" rx="1" fill="#fff"/></svg>
      </div>
    </div>
    <nav class="nav-bar">
      <svg class="back" width="18" height="32" viewBox="0 0 18 32" fill="none" stroke="#fff" stroke-width="2.4" stroke-linecap="round"><path d="M16 2L3 16l13 14"/></svg>
      <h1>Offensive 2 vs. 1</h1>
    </nav>
  </header>

  <div class="timeline-rail"></div>

  <div class="media hero" role="img" aria-label="Photo of a player in a yellow number 10 shirt celebrating on the pitch"></div>
  <div class="divider" style="top:320px"></div>

  <div class="node" style="top:332px">
    <svg width="22" height="22" viewBox="0 0 22 22" fill="none" stroke="#fff" stroke-width="1.6"><rect x="2" y="4" width="15" height="15"/><path d="M8 14l1-4 9-9 3 3-9 9z"/></svg>
  </div>
  <h2 class="drill-title">Offensive 2 vs. 1</h2>
  <p class="copy intro">Lorem ipsum dolor sit amet, consectetur adipisicing elit, sed do eiusmod tempor incidi dunt&nbsp; labore et dolore magna aliqua. Ut enim ad minim veniam, quis nost ex ercitation ullamco laboris nisi ut aliquip ex ea commodo consequat. Duis aute irure dolor in repr ehenderit in vluptate velit esse cillum dolore eu fugiat nulla par atur eaque ipsa quae ab illo inventore veritatis et quasi architecto beatae vitae dictasunt explicabo nemo enim ipsam voluptatem.</p>
  <div class="divider" style="top:548px"></div>

  <div class="node" style="top:574px">
    <svg width="24" height="20" viewBox="0 0 24 20" fill="none" stroke="#fff" stroke-width="1.6"><rect x="1" y="1" width="22" height="18"/><path d="M6 1v18M18 1v18M1 6h5M1 10h5M1 14h5M18 6h5M18 10h5M18 14h5"/><path d="M10 7l4 3-4 3z" fill="#fff"/></svg>
  </div>
  <div class="media video" role="img" aria-label="Training video still of players warming up on the pitch">
    <div class="play"><svg width="24" height="30" viewBox="0 0 24 30" fill="none" stroke="#fff" stroke-width="2"><path d="M3 2l19 13L3 28z"/></svg></div>
  </div>
  <p class="copy caption">Adipisicing elit, sed do eiusmod tempor incidi dunt&nbsp; labore et dolore magna aliqua. Ut enim ad minim veniam, quis nost ex ercitation ullamco laboris nisi ut aliquip ex ea commodo consequat.</p>
  <div class="divider" style="top:964px"></div>

  <div class="node" style="top:985px">
    <svg width="24" height="24" viewBox="0 0 24 24" fill="none" stroke="#fff" stroke-width="1.8" stroke-linecap="round"><path d="M10 14a4 4 0 0 0 6 0l4-4a4 4 0 0 0-6-6l-1.5 1.5"/><path d="M14 10a4 4 0 0 0-6 0l-4 4a4 4 0 0 0 6 6l1.5-1.5"/></svg>
  </div>
  <div class="resource">
    <div class="source">Cloudbox, shortlink</div>
    <a class="url" href="#">http://lnk.vx/4rtQmWa</a>
    <p class="note">Dolore magna aliquat enim ad minim veniam,</p>
  </div>

  <footer class="tab-bar">
    <div class="tab active">
      <svg width="40" height="40" viewBox="0 0 40 40" fill="none" stroke="currentColor" stroke-width="1.8"><circle cx="20" cy="20" r="18"/><path d="M20 17v11M17 28h6M17 17h3"/><circle cx="20" cy="12" r="1.3" fill="currentColor"/></svg>
      <span>Info</span>
    </div>
    <div class="tab">
      <svg width="34" height="40" viewBox="0 0 34 40" fill="none" stroke="currentColor" stroke-width="1.6"><rect x="3" y="6" width="28" height="32" rx="2"/><rect x="12" y="2" width="10" height="7" rx="1"/><path d="M11 18l4 4M15 18l-4 4M20 28l3-3 3 3M14 30c2-4 4-6 6-8"/></svg>
      <span>Skills</span>
    </div>
    <div class="tab">
      <svg width="44" height="40" viewBox="0 0 44 40" fill="none" stroke="currentColor" stroke-width="1.6"><path d="M14 4l-7 22h14z"/><path d="M9 18h10M11 12h6"/><path d="M30 14l-6 18h12z"/><path d="M26 25h8"/><path d="M2 30l20 8 20-6"/></svg>
      <span>Preq</span>
    </div>
    <div class="tab-indicator"></div>
  </footer>
</main>
</body>
</html>
```